Präsentationsvorlagen für Verkaufsgespräche
Zielgruppe
Wir verkaufen hochwertigen Kaffee, der traditionel im Trommelröster langsam geröstet wird. Unsere Zielgruppe sind W/ M 30-70.
Aufgabenstellung
Mit dieser Vorlage möchte ich bei den ersten Verkaufsgesprächen unsere Firma gut repräsentieren. Das wird keine lange Präsentation, soll aber einen ansprechenden Einstieg ins Gespräch sein.
Ein paar Fotos habe ich beigefügt. Texte füge ich später ein, wenn jemand was griffbereit hat, nehme ich aber auch das gerne.

```html
<!DOCTYPE html>
<html lang="de">
<head>
<meta charset="utf-8">
<title>Tostaro – Präsentationsvorlagen</title>
<link rel="stylesheet" href="https://fonts.googleapis.com/css2?family=Fira+Sans:wght@400;600&family=Amatic+SC:wght@700&display=swap">
<style>
  :root{
    --bg:#a9a9ab;
    --paper:#fdfcfa;
    --brown:#6b3f1c;
    --brown-dark:#3a2110;
    --ink:#2b1a0e;
    --white:#ffffff;
  }
  *{box-sizing:border-box;margin:0;padding:0}
  html,body{width:1200px;height:900px;overflow:hidden}
  body{background:var(--bg);font-family:"Fira Sans",sans-serif;color:var(--ink);position:relative}

  .brand-header{position:absolute;left:28px;top:40px;display:flex;align-items:center;gap:18px}
  .brand-header .dot{width:64px;height:64px;border-radius:50%;background:var(--white)}
  .brand-header .name{font-family:"Fira Sans",sans-serif;font-weight:600;font-size:64px;color:var(--white);line-height:1}

  .deck{position:absolute;left:28px;top:170px;display:grid;grid-template-columns:560px 560px;grid-template-rows:315px 315px;gap:24px}
  .slide{position:relative;width:560px;height:315px;overflow:hidden;background:var(--paper);box-shadow:0 6px 18px rgba(0,0,0,.35)}
  .photo{position:absolute;top:0;bottom:0;width:62%}
  .slide--text-right .photo{left:0}
  .slide--text-left .photo{right:0}
  .photo--espresso{background:linear-gradient(135deg,#2c2520 0%,#6e625a 40%,#c9a070 62%,#efeae4 100%)}
  .photo--bags{background:linear-gradient(120deg,#eef0f2 0%,#e4cf9e 35%,#c9a66a 60%,#f1e6cf 100%)}
  .photo--beans{background:linear-gradient(200deg,#1c0f0a 0%,#5a3320 45%,#8a5a3a 70%,#2a1710 100%)}
  .photo--hands{background:linear-gradient(160deg,#261611 0%,#7a4a33 45%,#b67d5c 65%,#3d2218 100%)}

  .shape{position:absolute;inset:0;width:100%;height:100%}
  .slide--text-left .shape{transform:scaleX(-1)}
  .shape .panel{fill:var(--paper)}
  .shape .band{fill:none;stroke:var(--brown);stroke-width:16}
  .shape .rule{fill:none;stroke:var(--white);stroke-width:2}

  .slide-mark{position:absolute;font-weight:600;font-size:20px;color:var(--white)}
  .slide--text-right .slide-mark{left:18px;bottom:16px}
  .slide--text-left .slide-mark{right:18px;top:14px}

  .copy{position:absolute;top:16px;bottom:14px;width:230px;font-size:9px;line-height:1.35;display:flex;flex-direction:column;gap:6px}
  .slide--text-right .copy{right:16px}
  .slide--text-left .copy{left:16px}
  .copy h2{font-family:"Amatic SC",sans-serif;font-weight:700;font-size:30px;line-height:1;color:var(--ink);letter-spacing:.5px}
</style>
</head>
<body>
  <header class="brand-header">
    <span class="dot"></span>
    <span class="name">Tostaro</span>
  </header>

  <main class="deck">
    <section class="slide slide--text-right">
      <div class="photo photo--espresso" role="img" aria-label="Foto: Espresso läuft aus dem Siebträger in eine weiße Tasse"></div>
      <svg class="shape" viewBox="0 0 560 315" aria-hidden="true">
        <path class="panel" d="M270,0 C330,70 270,200 340,315 L560,315 L560,0 Z"/>
        <path class="band" d="M252,0 C312,70 252,200 322,315"/>
        <path class="rule" d="M263,0 C323,70 263,200 333,315"/>
      </svg>
      <span class="slide-mark">Tostaro</span>
      <div class="copy">
        <p>Die Auswahl dieser Rohkaffees und das Mischen der Blends ist eine wesentliche Grundlage. Alles Wissen um den Einkauf wäre jedoch nichts wert ohne die Erfahrung und das handwerkliche Können der Röstkunst.</p>
        <p>Die Röstung erfolgt im klassischen traditionellen Trommel-Röstverfahren. Es ist nichts Neues mehr, daß dieses Röstverfahren schonend bei niedriger Temperatur erfolgt, die Bohnen konserviert.</p>
        <h2>Die Rösterei</h2>
        <p>Im Trommelröster verlieren die Bohnen fast ein Fünftel an Gewicht, aber sie gewinnen enorm an Geschmack und die Aromen entfalten sich besser.</p>
        <p>Je Blend und Sorte die ideale Balance von Säure, Süße und Bitterkeit zu erreichen, das ist die Kunst.</p>
      </div>
    </section>

    <section class="slide slide--text-right">
      <div class="photo photo--bags" role="img" aria-label="Foto: goldene Kaffeebeutel mit Ventil und Markenetikett"></div>
      <svg class="shape" viewBox="0 0 560 315" aria-hidden="true">
        <path class="panel" d="M270,0 C330,70 270,200 340,315 L560,315 L560,0 Z"/>
        <path class="band" d="M252,0 C312,70 252,200 322,315"/>
        <path class="rule" d="M263,0 C323,70 263,200 333,315"/>
      </svg>
      <span class="slide-mark">Tostaro</span>
      <div class="copy">
        <p>Tracibility – Rückverfolgbarkeit – ist unser Ziel.</p>
        <p>Wir möchten wissen aus welcher Region, welcher Ernte und welcher Plantage oder Kooperative unsere eingekauften Kaffees stammen.</p>
        <p>Ab einer Jahresmenge von 250 kg erstellen wir mit Ihnen gemeinsam eine eigene, auf Ihren Geschmack abgestimmte Mischung.</p>
      </div>
    </section>

    <section class="slide slide--text-left">
      <div class="photo photo--beans" role="img" aria-label="Foto: geröstete Kaffeebohnen vor dunklem Hintergrund"></div>
      <svg class="shape" viewBox="0 0 560 315" aria-hidden="true">
        <path class="panel" d="M270,0 C330,70 270,200 340,315 L560,315 L560,0 Z"/>
        <path class="band" d="M252,0 C312,70 252,200 322,315"/>
        <path class="rule" d="M263,0 C323,70 263,200 333,315"/>
      </svg>
      <span class="slide-mark">Tostaro</span>
      <div class="copy">
        <p>Für ein optimales Ergebnis in der Tasse ist das Wissen über alle wichtigen Parameter unumgänglich.</p>
        <p>Eine unserer wesentlichen Kompetenzen ist die laufende Schulung Ihrer Mitarbeiter, ob equipmenttechnisch oder bei den Zubereitungsarten. Wir laden Sie und Ihre Mitarbeiter ein, intensiv in die Welt des Kaffee einzutauchen und Ihr Wissen zu vertiefen.</p>
        <h2>Gastro &amp; Hotel</h2>
        <p>Unsere Schulungen finden in unserer an die Rösterei angeschlossenen Bar statt – praxisnah und individuell – um rasch und effizient ein perfektes Ergebnis in der Tasse zu erzielen. Mit Freude an der Sache und viel Spaß gehen Ihre Mitarbeiter danach motiviert wieder an die Sache heran und bekommen einen besseren Bezug zum Produkt.</p>
      </div>
    </section>

    <section class="slide slide--text-right">
      <div class="photo photo--hands" role="img" aria-label="Foto: zwei Hände halten geröstete Kaffeebohnen"></div>
      <svg class="shape" viewBox="0 0 560 315" aria-hidden="true">
        <path class="panel" d="M270,0 C330,70 270,200 340,315 L560,315 L560,0 Z"/>
        <path class="band" d="M252,0 C312,70 252,200 322,315"/>
        <path class="rule" d="M263,0 C323,70 263,200 333,315"/>
      </svg>
      <span class="slide-mark">Tostaro</span>
      <div class="copy">
        <p>Für Delikatessengeschäfte, Genussläden, Coffeeshops &amp; Elektropartner stellen wir ein ansprechendes Thekendisplay zur Verfügung.</p>
        <p>Wir versenden regelmäßig an einen großen Adressenverteiler unsere Liste der Bezugsquellen.</p>
        <h2>Feinkost</h2>
        <p>Wir verlinken Ihren Betrieb auf unserer Website. Fordern Sie ein unverbindliches Angebot an.</p>
      </div>
    </section>
  </main>
</body>
</html>
```